Business card for pediatric occupational therapist

I need a business card design for my independent occupational therapy company. I am a pediatric occupational therapist working with children 0-3 years of age. I would like the card to be clean (not too 'busy') and can include pictures/cartoon-like images of children, or toys such as building blocks, or other images that would be relevant to pediatric therapy. I want it to look professional but also intended to be clear that services provided are for children.
Target Market(s)
Families requiring occupational therapy services for their children (physical, emotional, social needs) - developmental delays
Industry/Entity Type
Rehabilitation
Contact Information for Business Card
Maren Tolsvik OT LLC
Maren Tolsvik, OTR/L
Occupational Therapist
maren.tolsvikOT@brindlemail.com

```html
<!DOCTYPE html>
<html lang="en">
<head>
<meta charset="utf-8">
<title>Maren Tolsvik OT LLC — Business Card</title>
<link rel="stylesheet" href="https://fonts.googleapis.com/css2?family=Poppins:wght@400;600;700&display=swap">
<style>
  :root {
    --stage: #e9e9ec;
    --card-white: #ffffff;
    --card-dark: #242426;
    --pink: #e6087f;
    --blue: #0a86d3;
    --ink: #3c3c3e;
    --muted-emboss: #4a4a4e;
    --photo-warm-a: #d9c6ad;
    --photo-warm-b: #b89a7a;
    --photo-cool-a: #e8e4df;
    --photo-cool-b: #b7c9c2;
    --photo-red-a: #efe8e2;
    --photo-red-b: #c9a79a;
  }
  * { box-sizing: border-box; margin: 0; padding: 0; }
  html, body { width: 1200px; height: 820px; overflow: hidden; }
  body {
    background: var(--stage);
    font-family: "Poppins", sans-serif;
    display: flex;
    flex-direction: column;
    align-items: center;
    justify-content: center;
    gap: 30px;
  }
  .card {
    position: relative;
    width: 640px;
    height: 366px;
    border-radius: 4px;
    overflow: hidden;
    box-shadow: 0 6px 18px rgba(0,0,0,.12);
  }
  .card--front {
    background: var(--card-white);
    border-bottom: 4px solid var(--pink);
    border-left: 2px solid var(--pink);
  }
  .card--back {
    background: var(--card-dark);
    border-bottom: 4px solid var(--pink);
    display: flex;
    align-items: center;
    justify-content: center;
  }

  /* brand mark */
  .brand {
    position: absolute;
    left: 44px;
    top: 70px;
    display: flex;
    align-items: center;
    gap: 10px;
  }
  .brand__dot {
    width: 22px; height: 22px;
    border-radius: 50%;
    background: var(--pink);
  }
  .brand__name {
    font-weight: 700;
    font-size: 20px;
    color: var(--pink);
    letter-spacing: .2px;
  }

  /* contact block */
  .contact {
    position: absolute;
    left: 44px;
    top: 176px;
    color: var(--ink);
  }
  .contact__name {
    font-size: 22px;
    font-weight: 400;
    line-height: 1.15;
  }
  .contact__first { color: var(--pink); font-weight: 700; }
  .contact__last { color: var(--blue); font-weight: 700; }
  .contact__role {
    font-size: 15px;
    margin-top: 2px;
  }
  .contact__lines {
    margin-top: 24px;
    display: flex;
    flex-direction: column;
    gap: 6px;
    font-size: 14.5px;
  }
  .contact__line { display: flex; align-items: center; gap: 8px; }
  .contact__icon { width: 16px; height: 16px; flex: none; }

  /* photo cluster */
  .photo {
    position: absolute;
    width: 176px; height: 176px;
    border-radius: 50%;
    border: 4px solid var(--card-white);
  }
  .photo--tower {
    left: 352px; top: 70px;
    background: radial-gradient(circle at 55% 60%, var(--photo-red-b), var(--photo-red-a) 70%);
  }
  .photo--blocks {
    left: 448px; top: 18px;
    background: radial-gradient(circle at 45% 50%, var(--photo-warm-b), var(--photo-warm-a) 75%);
  }
  .photo--floor {
    left: 440px; top: 160px;
    background: radial-gradient(circle at 50% 55%, var(--photo-cool-b), var(--photo-cool-a) 75%);
  }

  /* back side */
  .back-name {
    font-weight: 600;
    font-size: 26px;
    color: var(--muted-emboss);
    letter-spacing: .5px;
  }
</style>
</head>
<body>

  <section class="card card--front" aria-label="Business card front">
    <div class="brand">
      <span class="brand__dot"></span>
      <span class="brand__name">Maren Tolsvik OT LLC</span>
    </div>

    <div class="contact">
      <p class="contact__name"><span class="contact__first">Maren</span> <span class="contact__last">Tolsvik</span>, OTR/L</p>
      <p class="contact__role">Occupational Therapist</p>
      <div class="contact__lines">
        <p class="contact__line">
          <svg class="contact__icon" viewBox="0 0 24 24" aria-hidden="true">
            <path fill="var(--pink)" d="M6.6 10.8a15.1 15.1 0 0 0 6.6 6.6l2.2-2.2a1 1 0 0 1 1-.25 11.4 11.4 0 0 0 3.6.57 1 1 0 0 1 1 1V20a1 1 0 0 1-1 1A17 17 0 0 1 3 4a1 1 0 0 1 1-1h3.5a1 1 0 0 1 1 1c0 1.25.2 2.45.57 3.57a1 1 0 0 1-.25 1z"/>
          </svg>
          044-555 018 274
        </p>
        <p class="contact__line">
          <svg class="contact__icon" viewBox="0 0 24 24" aria-hidden="true">
            <rect x="2" y="5" width="20" height="14" rx="1.5" fill="var(--pink)"/>
            <path d="M3 6l9 7 9-7" fill="none" stroke="#fff" stroke-width="1.8"/>
          </svg>
          maren.tolsvikOT@brindlemail.com
        </p>
      </div>
    </div>

    <div class="photo photo--tower" role="img" aria-label="Photo of a toddler stacking a tower of coloured wooden blocks"></div>
    <div class="photo photo--blocks" role="img" aria-label="Photo of a young child playing with wooden blocks on a table"></div>
    <div class="photo photo--floor" role="img" aria-label="Photo of a toddler in overalls playing with blocks on the floor"></div>
  </section>

  <section class="card card--back" aria-label="Business card back">
    <p class="back-name">Maren Tolsvik OT LLC</p>
  </section>

</body>
</html>
```